Beef cattle farm needs signs which can be seen from roadside

We would like submissions of artwork for a sign that will hang from a fence or gate and will be seen by passing cars.

Existing logo and branding theme for the company is attached.

Signage can be between 900mm x 400mm - 1200mm x 600mm

Industry/Entity Type

Farm

Requirements
Must have
• the Signs should have the following information:
• Company name: Bellwin Grazing Company
• Address: 184 Tilbury Creek Road
• Contact number: 0491 362 815
• email address: admin@bellwingrazingco.example.com.au
• - Logo and branding as per attached artwork

```html
<!DOCTYPE html>
<html lang="en">
<head>
<meta charset="utf-8">
<title>Bellwin Grazing Company – Roadside Sign</title>
<link rel="stylesheet" href="https://fonts.googleapis.com/css2?family=Arimo:wght@400;700&display=swap">
<style>
  :root {
    --backdrop: #b9b6b7;
    --paddock-green: #126637;
    --edge-grey: #bcbdc0;
    --sign-white: #ffffff;
    --text-white: #ffffff;
  }
  * { margin: 0; padding: 0; box-sizing: border-box; }
  html, body {
    width: 1200px;
    height: 655px;
    overflow: hidden;
    background: var(--backdrop);
  }
  .canvas {
    position: relative;
    width: 1200px;
    height: 655px;
  }
  .sign {
    position: absolute;
    left: 109px;
    top: 109px;
    width: 981px;
    height: 436px;
    overflow: hidden;
  }
  .sign-panels {
    position: absolute;
    inset: 0;
    display: block;
  }
  .brand-mark {
    position: absolute;
    left: 119px;
    top: 34px;
    width: 230px;
    height: 230px;
    border-radius: 50%;
    background: var(--paddock-green);
  }
  .brand-name {
    position: absolute;
    left: 40px;
    top: 282px;
    width: 386px;
    text-align: center;
    font-family: "Arimo", Arial, sans-serif;
    font-weight: 700;
    color: var(--paddock-green);
    line-height: 1;
  }
  .brand-name .name-main {
    display: block;
    font-size: 62px;
    letter-spacing: 2px;
  }
  .brand-name .name-sub {
    display: block;
    margin-top: 12px;
    font-size: 24px;
    letter-spacing: 1.5px;
  }
  .contact {
    position: absolute;
    right: 33px;
    top: 281px;
    text-align: right;
    font-family: "Arimo", Arial, sans-serif;
    color: var(--text-white);
  }
  .contact .phone {
    font-size: 34px;
    font-weight: 700;
    line-height: 40px;
  }
  .contact .address {
    margin-top: 9px;
    font-size: 24px;
    font-weight: 400;
    line-height: 28px;
  }
  .contact .email {
    margin-top: 8px;
    font-size: 20px;
    font-weight: 700;
    line-height: 24px;
  }
</style>
</head>
<body>
  <div class="canvas">
    <div class="sign">
      <svg class="sign-panels" width="981" height="436" viewBox="0 0 981 436" aria-hidden="true">
        <rect class="panel-green" width="981" height="436" fill="var(--paddock-green)"/>
        <path class="panel-edge" d="M0 0 H445 A374 374 0 0 1 450 436 H0 Z" fill="var(--edge-grey)"/>
        <path class="panel-white" d="M0 0 H431 A374 374 0 0 1 436 436 H0 Z" fill="var(--sign-white)"/>
      </svg>

      <div class="brand-mark"></div>
      <div class="brand-name">
        <span class="name-main">BELLWIN</span>
        <span class="name-sub">GRAZING COMPANY</span>
      </div>

      <div class="contact">
        <p class="phone">Call : 0491 362 815</p>
        <p class="address">184 Tilbury Creek Road</p>
        <p class="email">admin@bellwingrazingco.example.com.au</p>
      </div>
    </div>
  </div>
</body>
</html>
```